Edit of flyers - text to be eddited

I currently have three flyers already designed, but want to edit the text on them. On the front of each flyer I want to delete the text which states: "50% off lawn mowing applies to first lawn mowed on any regular service and applies to first 100 callers so call now" and replace it with "Professional Lawn and Garden Maintenance".

Also on the front and rear of each flyer I want to replace the text which states "Leo and Martin" with "Martin Hollis."

All other details can stay the same thanks. I need each of the files saved as a pdf according to the instructions attached with the bleed area set as specified for printing.

Font styles to use
Serif

Colors
acd036
fbed22

Requirements
Must have
• On the front of each flyer I want to delete the text which states: "50% off lawn mowing applies to first lawn mowed on any regular service and applies to first 100 callers so call now" and replace it with "Professional Lawn and Garden Maintenance".
• Also on the front and rear of each flyer I want to replace the text which states "Leo and Martin" with "Martin Hollis."
• All other details can stay the same thanks. I need each of the files saved as a pdf according to the instructions attached with the bleed area set as specified for printing.

```html
<!DOCTYPE html>
<html lang="en">
<head>
<meta charset="utf-8">
<title>Liberty Yards – Flyer Front and Back</title>
<link href="https://fonts.googleapis.com/css2?family=Lobster+Two:ital,wght@0,700;1,700&family=Nunito:wght@800&family=Open+Sans:wght@400;600;700&display=swap" rel="stylesheet">
<style>
  :root {
    --board: #505050;
    --white: #ffffff;
    --brand-green: #1e8a3c;
    --lime: #acd036;
    --lime-deep: #9cc43a;
    --yellow: #fbed22;
    --orange: #f5922a;
    --sign-dark: #1f8a45;
    --sign-light: #9cc845;
    --band: rgba(140, 180, 40, 0.78);
  }
  * { margin: 0; padding: 0; box-sizing: border-box; }
  html, body { width: 900px; height: 1200px; overflow: hidden; }
  body {
    position: relative;
    background: var(--board);
    font-family: "Open Sans", Arial, sans-serif;
  }
  .side-label {
    position: absolute;
    left: 0; width: 900px;
    text-align: center;
    color: var(--white);
    font-family: Arial, Helvetica, sans-serif;
    font-size: 50px;
    letter-spacing: 1px;
  }
  .side-label--front { top: 560px; }
  .side-label--back { top: 1085px; }

  .card {
    position: absolute;
    overflow: hidden;
    box-shadow: 0 4px 12px rgba(0,0,0,0.35);
  }

  /* FRONT */
  .card--front { left: 57px; top: 133px; width: 786px; height: 379px; background: var(--white); }
  .front-brand-panel {
    position: absolute; left: 0; top: 0; width: 273px; height: 379px; background: var(--white);
  }
  .brand-mark {
    position: absolute; left: 0; top: 170px; width: 273px;
    display: flex; align-items: center; justify-content: center; gap: 10px;
  }
  .brand-mark__square { width: 22px; height: 22px; background: var(--brand-green); }
  .brand-mark__name {
    font-family: "Lobster Two", Georgia, serif; font-weight: 700; font-style: normal;
    font-size: 32px; color: var(--brand-green);
  }
  .front-tagline {
    position: absolute; left: 0; top: 335px; width: 273px; text-align: center;
    font-family: "Lobster Two", Georgia, serif; font-style: italic; font-weight: 700;
    font-size: 18px; color: var(--brand-green);
  }
  .front-photo {
    position: absolute; left: 273px; top: 0; width: 513px; height: 379px;
    background:
      radial-gradient(circle at 400px 75px, rgba(255,255,235,0.95) 0, rgba(255,240,170,0.7) 45px, rgba(255,220,110,0) 150px),
      linear-gradient(180deg, #f0a43a 0%, #f6c65a 12%, #fbe383 20%, #d7d86a 23%, #7da83a 26%, #a9cc3c 40%, #7fb52c 65%, #4f8f1c 100%);
  }
  .front-pointer { position: absolute; left: 273px; width: 0; height: 0;
    border-top: 12px solid transparent; border-bottom: 12px solid transparent; border-left: 20px solid var(--white); }
  .front-pointer--one { top: 112px; }
  .front-pointer--two { top: 160px; }
  .service-band {
    position: absolute; left: 306px; height: 41px; border-radius: 6px; background: var(--band);
    color: var(--white); font-family: "Lobster Two", Georgia, serif; font-style: italic; font-weight: 700;
    font-size: 33px; line-height: 40px; padding-left: 24px;
  }
  .service-band--one { top: 102px; width: 317px; }
  .service-band--two { top: 150px; width: 372px; }
  .front-offer {
    position: absolute; left: 311px; top: 212px;
    font-family: "Nunito", Arial, sans-serif; font-weight: 800; font-size: 27px; line-height: 34px;
    color: var(--orange);
    text-shadow: 1px 1px 0 #fff, -1px -1px 0 #fff, 1px -1px 0 #fff, -1px 1px 0 #fff, 0 2px 0 #fff;
  }
  .front-contact {
    position: absolute; right: 25px; top: 277px; text-align: right; color: var(--white);
  }
  .front-contact__name { font-size: 13px; line-height: 18px; margin-bottom: 10px; }
  .front-contact__phone { font-size: 19px; font-weight: 600; line-height: 24px; }
  .front-contact__email { font-size: 10px; font-weight: 600; line-height: 16px; }
  .front-contact__web { font-size: 12px; font-weight: 700; line-height: 16px; }

  /* BACK */
  .card--back { left: 43px; top: 657px; width: 790px; height: 380px; }
  .back-photo {
    position: absolute; inset: 0;
    background:
      radial-gradient(ellipse 160px 50px at 560px 120px, rgba(255,255,255,0.85), rgba(255,255,255,0)),
      radial-gradient(ellipse 200px 60px at 160px 40px, rgba(255,255,255,0.8), rgba(255,255,255,0)),
      linear-gradient(180deg, #4aa6e2 0%, #8fc8ee 30%, #e4f2fa 47%, #3f7f3a 50%, #4c8f33 55%, #8cc63e 60%, #6fb534 78%, #2f8c2a 100%);
  }
  .back-intro {
    position: absolute; left: 17px; top: 18px;
    font-family: "Lobster Two", Georgia, serif; font-style: italic; font-weight: 700;
    font-size: 22px; line-height: 30px; color: var(--brand-green);
    text-shadow: 1px 1px 0 #fff, -1px -1px 0 #fff, 1px -1px 0 #fff, -1px 1px 0 #fff;
  }
  .back-contact { position: absolute; right: 15px; top: 12px; text-align: right; }
  .back-contact__name {
    font-family: "Lobster Two", Georgia, serif; font-weight: 700; font-style: italic;
    font-size: 32px; line-height: 38px; color: var(--brand-green);
    text-shadow: 0 0 3px rgba(255,255,255,0.9);
  }
  .back-contact__phone, .back-contact__web {
    font-size: 24px; font-weight: 600; line-height: 34px; color: var(--lime-deep);
    text-shadow: 1px 1px 0 #fff, -1px -1px 0 #fff, 1px -1px 0 #fff, -1px 1px 0 #fff;
  }
  .back-closing {
    position: absolute; left: 385px; top: 293px;
    font-family: "Lobster Two", Georgia, serif; font-style: italic; font-weight: 700;
    font-size: 22px; line-height: 30px; color: var(--white);
    text-shadow: 0 1px 2px rgba(0,0,0,0.3);
  }
  .signposts { position: absolute; left: 0; top: 0; }
  .signposts .post { fill: var(--sign-light); }
  .signposts .sign--dark { fill: var(--sign-dark); }
  .signposts .sign--light { fill: var(--sign-light); }
  .signposts text { font-family: "Open Sans", Arial, sans-serif; font-weight: 700; font-size: 14px; text-anchor: middle; }
  .signposts text.label--small { font-size: 11px; }
  .signposts .label--dark { fill: var(--yellow); }
  .signposts .label--light { fill: var(--white); }
</style>
</head>
<body>

<section class="card card--front" aria-label="Flyer front">
  <div class="front-brand-panel">
    <div class="brand-mark">
      <span class="brand-mark__square"></span>
      <span class="brand-mark__name">Liberty Yards</span>
    </div>
    <p class="front-tagline">Lawn and Garden Maintenance</p>
  </div>
  <div class="front-photo" role="img" aria-label="Photo of a sunlit green meadow with wildflowers under an orange sunrise sky"></div>
  <span class="front-pointer front-pointer--one"></span>
  <span class="front-pointer front-pointer--two"></span>
  <div class="service-band service-band--one">professional lawn</div>
  <div class="service-band service-band--two">garden maintenance</div>
  <p class="front-offer">Professional lawn mowing<br>at an affordable price.</p>
  <div class="front-contact">
    <p class="front-contact__name">Martin Hollis</p>
    <p class="front-contact__phone">Ph:0400555218</p>
    <p class="front-contact__email">Email: libertyyards@mailbox.com</p>
    <p class="front-contact__web">www.libertyyards.com.au</p>
  </div>
</section>
<p class="side-label side-label--front">FRONT</p>

<section class="card card--back" aria-label="Flyer back">
  <div class="back-photo" role="img" aria-label="Photo of a wide green lawn with a tree line under a blue sky with white clouds"></div>
  <p class="back-intro">At Liberty Yards we specialise in<br>the following services;</p>
  <div class="back-contact">
    <p class="back-contact__name">Liberty Yards</p>
    <p class="back-contact__phone">Ph 0400555218</p>
    <p class="back-contact__web">www.libertyyards.com.au</p>
  </div>
  <svg class="signposts" width="790" height="380" viewBox="0 0 790 380" aria-label="Service signposts">
    <rect class="post" x="74" y="88" width="16" height="292"/>
    <rect class="post" x="287" y="88" width="16" height="292"/>

    <polygon class="sign--light" points="27,132 37,120 179,120 179,144 37,144"/>
    <text class="label--light" x="106" y="137">Lawn mowing</text>
    <polygon class="sign--dark" points="27,166 37,154 179,154 179,178 37,178"/>
    <text class="label--dark" x="108" y="171">Edging</text>
    <polygon class="sign--light" points="27,196 37,184 179,184 179,208 37,208"/>
    <text class="label--light" x="108" y="201">Blowing</text>
    <polygon class="sign--dark" points="25,215 169,215 179,227 169,239 25,239"/>
    <text class="label--dark" x="100" y="232">Hedging</text>
    <polygon class="sign--light" points="27,244 169,244 179,256 169,268 27,268"/>
    <text class="label--light" x="100" y="261">Pruning</text>
    <polygon class="sign--light" points="27,284 37,272 179,272 179,296 37,296"/>
    <text class="label--light" x="106" y="289">Tree Loping</text>
    <polygon class="sign--dark" points="27,314 37,302 179,302 179,326 37,326"/>
    <text class="label--dark" x="106" y="319">Weeding</text>

    <polygon class="sign--dark" points="213,121 355,121 365,133 355,145 213,145"/>
    <text class="label--dark" x="284" y="138">Poisoning</text>
    <polygon class="sign--light" points="213,165 223,153 365,153 365,177 223,177"/>
    <text class="label--light" x="292" y="170">Mulching</text>
    <polygon class="sign--dark" points="213,198 223,186 365,186 365,210 223,210"/>
    <text class="label--dark" x="292" y="203">Fertilising</text>
    <polygon class="sign--light" points="213,229 223,217 365,217 365,241 223,241"/>
    <text class="label--light" x="294" y="234">Rubbish removal</text>
    <polygon class="sign--dark" points="213,245 355,245 365,257 355,269 213,269"/>
    <text class="label--dark" x="284" y="262">Planting</text>
    <rect class="sign--light" x="213" y="274" width="152" height="24"/>
    <text class="label--light label--small" x="289" y="290">Lawn care and advice</text>
    <polygon class="sign--light" points="213,302 355,302 365,314 355,326 213,326"/>
    <text class="label--light" x="280" y="319">Turf</text>
  </svg>
  <p class="back-closing">And any other garden maintenance job,<br>No job too big or too small.</p>
</section>
<p class="side-label side-label--back">BACK</p>

</body>
</html>
```